unique professional wordpress website design for high end limo rental / car rental company

We need a elegant and professional website (ready to use wordpress theme) for a Car rental / Transport services company. We provide luxury cars on rental and lease. Website needs to be unique, high end and classy and should project the brand name and value proposition. It should not be similar to any existing websites with the same or similar brand name and category. Files should be as a ready to use wordpress 4.7 compatible theme file and should include images and video (stock footage) or links to the stock items used.

Home page should have a full width video background similar to the link below. Something similar can be used.

https://www.clipstreamexample.com/watch?v=9qrT_avbx3K

Menu Structure:
Home (Video background, menu)

Vehicles (banner, two column design with alternate image and content)

Services ( Events, Shuttle Services, Airport Limo, Executive Limo, Point to Point) Seperate page for each sub menu with 2 column content and image

Prices (Drop down selection for start point and end point) also can be selected from map.

Gallery (Video and image gallery - Thumbnail view)

About us : Content and images in alternating blocks

Contact Us : Address, contact details, location map, and Contact us form (Name, email address, Mobile phone, Query / Question) and send button. to be connected to email address later.

Website Footer to have the following (Testimonials single line text moving), Social media icons along with likes / tweets number only, and hyperlink. Contact address, and Newsletter subscription.

Book now Button will lead to the Booking page and payment gateway. Will be done seperately

Header will have Contact numbers, Access email (Button) Book now (Button)

Company : Velour Limousine
domain : https://www.velour.limo
Sector : Transport solutions, taxi, vehicle rental, chauffer services
Preferred colors : Blue, White, Gold, Black

Files should be compatible with Wordpress 4.7, and should optionally have html/css included along with stock images and video / links.

Target Market(s)

B2B, Transport

Industry/Entity Type

Travel Industry

Font styles to use
Serif
Sans Serif

Requirements
Must have
• Wordpress theme files, HTML/CSS, images and video (links)
Nice to have
• ecommerce page design for cab booking, similar to this:
• https://book.velourcarsexample.com/RideDeskApp/FastBooking?y
Should not have
• no copy paste or using existing commercial wordpress templates.

```html
<!DOCTYPE html>
<html lang="en">
<head>
<meta charset="utf-8">
<title>Velour Limousine</title>
<link href="https://fonts.googleapis.com/css2?family=Libre+Baskerville:wght@400;700&family=Montserrat:wght@700;800&family=Roboto:wght@400;500;700&display=swap" rel="stylesheet">
<style>
:root{
  --gold:#c4922e;
  --gold-dark:#a97c22;
  --black:#000;
  --ink:#222;
  --muted:#666;
  --blue:#2e4f8a;
  --light:#f6f6f6;
  --white:#fff;
}
*{box-sizing:border-box;margin:0;padding:0}
html,body{width:1200px;height:2571px;overflow:hidden;background:var(--white)}
body{position:relative;font-family:'Roboto',sans-serif;color:var(--ink)}
section,header,footer{position:absolute;left:0;width:1200px}

/* Header */
.site-header{top:0;height:123px;background:var(--black)}
.brand{position:absolute;left:98px;top:28px;width:120px;text-align:center}
.brand-mark{display:block;width:34px;height:34px;margin:0 auto 8px;border:2px solid var(--gold);border-radius:50%}
.brand-name{font-family:'Libre Baskerville',serif;font-size:26px;color:var(--gold);letter-spacing:1px}
.header-top{position:absolute;right:98px;top:20px;display:flex;align-items:center;gap:14px}
.phone{display:flex;align-items:center;gap:14px;color:var(--white);font-weight:700;font-size:23px;margin-right:36px}
.btn{display:inline-block;font-size:12px;text-transform:uppercase;padding:10px 16px;color:var(--white)}
.btn-gold{background:var(--gold)}
.btn-outline{border:1.5px solid var(--white)}
.main-nav{position:absolute;right:98px;top:80px;display:flex;gap:46px}
.main-nav a{color:#ddd;font-size:12px;text-transform:uppercase;text-decoration:none}

/* Hero */
.hero{top:123px;height:474px;overflow:hidden}
.hero-media{position:absolute;inset:0;background:radial-gradient(ellipse at 60% 55%,#7a1e22 0%,#3e2628 30%,#4b4a4a 60%,#2a2a2a 100%)}
.hero-title{position:absolute;top:112px;width:100%;text-align:center;font-family:'Montserrat',sans-serif;font-weight:800;font-size:88px;color:var(--white);text-shadow:3px 3px 0 rgba(0,0,0,.6)}
.hero-sub{position:absolute;top:222px;width:100%;text-align:center;font-size:20px;color:var(--white)}
.hero-play{position:absolute;left:573px;top:289px}
.hero-arrow{position:absolute;top:196px}

/* Section titles */
.section-title{font-family:'Libre Baskerville',serif;font-weight:700;font-size:29px;text-transform:uppercase;color:#111}

/* Services */
.services{top:597px;height:456px}
.services .section-title{position:absolute;top:64px;width:100%;text-align:center}
.service{position:absolute;top:140px;width:262px;text-align:center}
.service svg{display:block;margin:0 auto}
.service h3{font-size:21px;font-weight:500;text-transform:uppercase;margin-top:20px;color:#111}
.service p{font-size:12.5px;line-height:24px;color:var(--muted);margin-top:12px}
.read-more{display:block;margin-top:10px;font-size:11.5px;font-weight:700;color:var(--gold);text-transform:uppercase}

/* Split blocks */
.split{height:428px}
.split .panel{position:absolute;top:0;width:600px;height:428px;background:var(--light)}
.split .media{position:absolute;top:0;width:600px;height:428px}
.about{top:1053px}
.about .panel{left:0}
.about .media{left:600px;background:linear-gradient(120deg,#4b5767 0%,#8d96a4 45%,#d1a46a 75%,#5a5e66 100%)}
.vehicles{top:1481px}
.vehicles .panel{left:600px}
.vehicles .media{left:0;background:linear-gradient(180deg,#c9c9cc 0%,#7d8796 40%,#5b2d30 60%,#3b3c40 100%)}
.panel-inner{position:absolute;left:98px;top:72px;width:420px}
.vehicles .panel-inner{left:87px;width:430px}
.lead{color:var(--blue);font-size:14px;line-height:26px;margin-top:24px}
.vehicles .lead{color:#222}
.body-copy{font-size:12.5px;line-height:25px;color:var(--muted);margin-top:14px}
.btn-block{display:inline-block;background:var(--gold);color:var(--white);font-size:12px;text-transform:uppercase;padding:11px 16px;margin-top:42px}
.about .btn-block{margin-top:40px}
.ticks{list-style:none;margin-top:22px}
.ticks li{position:relative;padding-left:28px;font-size:12.5px;color:var(--muted);line-height:34.5px;white-space:nowrap}
.ticks li::before{content:"»";position:absolute;left:0;color:var(--blue);font-size:14px}

/* Gallery */
.gallery{top:1910px;height:356px}
.gallery .section-title{position:absolute;top:64px;width:100%;text-align:center}
.thumbs{position:absolute;top:137px;left:98px;display:flex;gap:20px}
.thumb{position:relative;width:235px;height:146px;border-radius:3px;display:flex;align-items:center;justify-content:center}
.t1{background:linear-gradient(160deg,#6d6b68,#3d4b55 60%,#8b8d90)}
.t2{background:linear-gradient(160deg,#8b8a88,#4a4a48 60%,#6f6e6a)}
.t3{background:linear-gradient(160deg,#5e5d5b,#2e2e30 55%,#8c8a86)}
.t4{background:linear-gradient(160deg,#9ea4ad,#3a3e45 55%,#c78d52)}

/* Footer */
.site-footer{top:2266px;height:254px;background:var(--gold)}
.foot-col{position:absolute;top:52px;color:var(--white)}
.foot-col h4{font-size:16px;font-weight:500;text-transform:uppercase;margin-bottom:18px}
.contact-list{list-style:none;font-size:12px}
.contact-list li{display:flex;align-items:center;gap:22px;height:33px}
.contact-list svg{flex:0 0 12px}
.social{display:flex;gap:26px;font-size:12px;align-items:center}
.social span{display:flex;align-items:center;gap:10px}
.quote{font-size:12px;line-height:22px;width:230px}
.reviewer{display:flex;align-items:center;gap:18px;margin-top:18px}
.avatar{width:52px;height:52px;border-radius:50%;background:linear-gradient(#e9e4dc,#b9b2a6);border:2px solid var(--white)}
.reviewer b{display:block;font-size:14px;font-weight:500;text-transform:uppercase}
.reviewer small{font-size:12px}
.signup{font-size:12px;text-transform:uppercase;margin-bottom:14px}
.subscribe{display:flex;width:248px;height:36px}
.subscribe .field{flex:1;background:var(--white);font-size:11px;color:#aaa;font-style:italic;padding:11px 14px}
.subscribe .send{width:40px;background:var(--blue);display:flex;align-items:center;justify-content:center}
.copyright{position:absolute;top:2520px;left:0;width:1200px;height:51px;background:var(--gold-dark);color:var(--white);font-size:12px;text-align:center;line-height:51px}
</style>
</head>
<body>

<header class="site-header">
  <div class="brand"><span class="brand-mark"></span><span class="brand-name">VELOUR</span></div>
  <div class="header-top">
    <span class="phone">
      <svg width="20" height="20" viewBox="0 0 20 20"><rect width="20" height="20" rx="3" fill="#c4922e"/><path d="M6 5l2 0 1 3-1.5 1a7 7 0 0 0 3.5 3.5L12 11l3 1v2a1 1 0 0 1-1 1A10 10 0 0 1 5 6a1 1 0 0 1 1-1z" fill="#000"/></svg>
      555 010 2020
    </span>
    <span class="btn btn-gold">Access Email</span>
    <span class="btn btn-outline">Book Now</span>
  </div>
  <nav class="main-nav">
    <a>Home</a><a>Vehicles</a><a>Services</a><a>Prices</a><a>Gallery</a><a>About Us</a><a>Contact Us</a>
  </nav>
</header>

<section class="hero">
  <div class="hero-media" role="img" aria-label="Red luxury sports saloon driving fast on a motorway, motion-blurred background"></div>
  <h1 class="hero-title">THE VELOUR</h1>
  <p class="hero-sub">We provide luxury cars on rental and lease.</p>
  <svg class="hero-play" width="54" height="54" viewBox="0 0 54 54"><circle cx="27" cy="27" r="25" fill="none" stroke="#fff" stroke-width="2.5"/><circle cx="27" cy="27" r="16" fill="none" stroke="#fff" stroke-width="2"/><path d="M23 20l10 7-10 7z" fill="none" stroke="#fff" stroke-width="2"/></svg>
  <svg class="hero-arrow" style="left:48px" width="34" height="70" viewBox="0 0 34 70"><path d="M30 2L4 35l26 33" fill="none" stroke="#ccc" stroke-width="2"/></svg>
  <svg class="hero-arrow" style="right:48px" width="34" height="70" viewBox="0 0 34 70"><path d="M4 2l26 33L4 68" fill="none" stroke="#ccc" stroke-width="2"/></svg>
</section>

<section class="services">
  <h2 class="section-title">Our Services</h2>

  <div class="service" style="left:75px">
    <svg width="122" height="122" viewBox="0 0 122 122"><rect x="22" y="22" width="78" height="78" transform="rotate(45 61 61)" fill="#c4922e"/><rect x="18" y="18" width="86" height="86" transform="rotate(45 61 61)" fill="none" stroke="#c4922e" stroke-width="1.2"/><rect x="48" y="49" width="26" height="24" rx="2" fill="none" stroke="#fff" stroke-width="2.5"/><path d="M48 55h26M54 45v7M68 45v7M53 60h4M59 60h4M65 60h4M53 66h4M59 66h4M65 66h4" stroke="#fff" stroke-width="2.5"/></svg>
    <h3>Our Events</h3>
    <p>It is a long established fact that a reader<br>will be distracted by the readable</p>
    <span class="read-more">Read More</span>
  </div>

  <div class="service" style="left:337px">
    <svg width="122" height="122" viewBox="0 0 122 122"><rect x="22" y="22" width="78" height="78" transform="rotate(45 61 61)" fill="#c4922e"/><rect x="18" y="18" width="86" height="86" transform="rotate(45 61 61)" fill="none" stroke="#c4922e" stroke-width="1.2"/><path d="M47 60l26-12-8 26-6-9z M59 65l14-17" fill="none" stroke="#fff" stroke-width="2.5" stroke-linejoin="round"/></svg>
    <h3>Shuttle Services</h3>
    <p>It is a long established fact that a reader<br>will be distracted by the readable</p>
    <span class="read-more">Read More</span>
  </div>

  <div class="service" style="left:599px">
    <svg width="122" height="122" viewBox="0 0 122 122"><rect x="22" y="22" width="78" height="78" transform="rotate(45 61 61)" fill="#c4922e"/><rect x="18" y="18" width="86" height="86" transform="rotate(45 61 61)" fill="none" stroke="#c4922e" stroke-width="1.2"/><path d="M72 48c2-2 4-2 4 0s-2 3-4 5l-5 5 3 14-3 2-5-11-6 6 1 5-2 1-3-6-6-3 1-2 5 1 6-6-11-5 2-3 14 3z" fill="#fff"/></svg>
    <h3>Airport Limo</h3>
    <p>It is a long established fact that a reader<br>will be distracted by the readable</p>
    <span class="read-more">Read More</span>
  </div>

  <div class="service" style="left:862px">
    <svg width="122" height="122" viewBox="0 0 122 122"><rect x="22" y="22" width="78" height="78" transform="rotate(45 61 61)" fill="#c4922e"/><rect x="18" y="18" width="86" height="86" transform="rotate(45 61 61)" fill="none" stroke="#c4922e" stroke-width="1.2"/><rect x="46" y="52" width="30" height="20" rx="2" fill="#fff"/><path d="M55 52v-4h12v4" fill="none" stroke="#fff" stroke-width="2.5"/><path d="M46 61h30" stroke="#c4922e" stroke-width="2"/><rect x="58" y="59" width="6" height="5" fill="#c4922e"/></svg>
    <h3>Executive Limo</h3>
    <p>It is a long established fact that a reader<br>will be distracted by the readable</p>
    <span class="read-more">Read More</span>
  </div>
</section>

<section class="split about">
  <div class="panel">
    <div class="panel-inner">
      <h2 class="section-title">About Us</h2>
      <p class="lead">Contrary to popular belief, Lorem Ipsum is not simply random text.<br>It has roots in a piece of classical Latin literature</p>
      <p class="body-copy">There are many variations of passages of Lorem Ipsum available, but the majority have suffered alteration in some form, by injected humour, or randomised words which don't look even slightly believable. If you are going to use a passage of Lorem Ipsum, you need to be sure there isn't anything</p>
      <span class="btn-block">Read More</span>
    </div>
  </div>
  <div class="media" role="img" aria-label="Hand holding car keys beside a silver car door at sunset on a city street"></div>
</section>

<section class="split vehicles">
  <div class="media" role="img" aria-label="Rear view of a dark red sports car on an open road with yellow lane lines"></div>
  <div class="panel">
    <div class="panel-inner">
      <h2 class="section-title">Vehicles</h2>
      <p class="lead">Contrary to popular belief, Lorem Ipsum is not simply random text.<br>It has roots in a piece of classical Latin literature</p>
      <ul class="ticks">
        <li>Ullamco laboris nisi ut aliquip ex ea commodo consequat.</li>
        <li>Duis aute irure dolor in reprehenderit in voluptate velit esse cillum do</li>
        <li>Excepteur sint occaecat cupidatat non proident, sunt in culpa</li>
      </ul>
      <span class="btn-block">Read More</span>
    </div>
  </div>
</section>

<section class="gallery">
  <h2 class="section-title">Our Gallery</h2>
  <div class="thumbs">
    <div class="thumb t1" role="img" aria-label="Video: white car on a winding road">
      <svg width="40" height="40" viewBox="0 0 40 40"><circle cx="20" cy="20" r="17" fill="none" stroke="#fff" stroke-width="2"/><path d="M16 13l11 7-11 7z" fill="none" stroke="#fff" stroke-width="2"/></svg>
    </div>
    <div class="thumb t2" role="img" aria-label="Car on a motorway beside a guardrail"></div>
    <div class="thumb t3" role="img" aria-label="Video: close-up of a car headlight">
      <svg width="40" height="40" viewBox="0 0 40 40"><circle cx="20" cy="20" r="17" fill="none" stroke="#fff" stroke-width="2"/><path d="M16 13l11 7-11 7z" fill="none" stroke="#fff" stroke-width="2"/></svg>
    </div>
    <div class="thumb t4" role="img" aria-label="Car interior dashboard and steering wheel"></div>
  </div>
</section>

<footer class="site-footer">
  <div class="foot-col" style="left:98px">
    <h4>Contact Information</h4>
    <ul class="contact-list">
      <li><svg width="12" height="14" viewBox="0 0 10 14"><path d="M5 0a5 5 0 0 1 5 5c0 4-5 9-5 9S0 9 0 5a5 5 0 0 1 5-5z" fill="#fff"/><circle cx="5" cy="5" r="2" fill="#c4922e"/></svg>Harbourview, NSW</li>
      <li><svg width="12" height="12" viewBox="0 0 20 20"><path d="M4 1l4 0 2 5-3 2a11 11 0 0 0 5 5l2-3 5 2v4a2 2 0 0 1-2 2A17 17 0 0 1 1 4a2 2 0 0 1 2-3z" fill="#fff"/></svg>Phone - 0400 555 010</li>
      <li><svg width="12" height="12" viewBox="0 0 12 12"><rect x="0" y="4" width="12" height="6" fill="#fff"/><rect x="3" y="0" width="6" height="4" fill="#fff"/><rect x="3" y="8" width="6" height="4" fill="#fff" stroke="#c4922e"/></svg>Fax - 555 014 7788</li>
      <li><svg width="12" height="10" viewBox="0 0 12 10"><rect x=".5" y=".5" width="11" height="9" fill="none" stroke="#fff"/><path d="M.5 .5l5.5 5 5.5-5" fill="none" stroke="#fff"/></svg>E-mail - info@velourdemo.com</li>
    </ul>
  </div>
  <div class="foot-col" style="left:353px">
    <h4>Social Media</h4>
    <div class="social">
      <span><svg width="12" height="11" viewBox="0 0 12 11" aria-label="Likes"><path d="M6 11L1 6A3 3 0 0 1 6 2a3 3 0 0 1 5 4z" fill="#fff"/></svg>25k</span>
      <span><svg width="12" height="11" viewBox="0 0 12 11" aria-label="Shares"><path d="M1 1h10v7H5l-3 3V8H1z" fill="#fff"/></svg>25k</span>
      <span><svg width="12" height="11" viewBox="0 0 12 11" aria-label="Followers"><circle cx="6" cy="3" r="2.6" fill="#fff"/><path d="M1 11a5 4.5 0 0 1 10 0z" fill="#fff"/></svg>25k</span>
    </div>
  </div>
  <div class="foot-col" style="left:591px">
    <h4>Testimonial</h4>
    <p class="quote">" Sed ut perspiciatis unde omnis iste natus error sit voluptatem accusantium "</p>
    <div class="reviewer">
      <div class="avatar" role="img" aria-label="Client portrait"></div>
      <div><b>Daniel Morrow</b><small>- Management accounting</small></div>
    </div>
  </div>
  <div class="foot-col" style="left:852px">
    <h4>Newsletter</h4>
    <p class="signup">Sign up for a free week!</p>
    <div class="subscribe">
      <span class="field">Enter Your Mail Id</span>
      <span class="send"><svg width="14" height="14" viewBox="0 0 14 14"><path d="M0 6L14 0 10 14 7 8z" fill="#fff"/></svg></span>
    </div>
  </div>
</footer>
<div class="copyright">Copyrights@2017Company Name , All rights Reserved</div>

</body>
</html>
```